Ridgeline Talent Associates Business Card Design

We need a business card design for our new company - Ridgeline Talent Associates. RLTA is a recruitment firm that focuses on recruiting engineers and geologist for mid-size oil and gas companies. We would like our logo on the business card, which is attached, and we would like the color scheme on business cards to coordinate with our logo.

Industry/Entity Type

Oil And Gas

Contact Information for Business Card

Dana Whitlow, Founder and Managing Partner, dmw@ridgelinetalentco.org, 888.507.3942 (work), 5730915.0600 (cell), 573.642.1907 (fax), www.ridgelinetalentco.org

```html
<!DOCTYPE html>
<html lang="en">
<head>
<meta charset="utf-8">
<title>Ridgeline Talent Associates — Business Card</title>
<link rel="stylesheet" href="https://fonts.googleapis.com/css2?family=Sorts+Mill+Goudy&display=swap">
<style>
  :root {
    --page: #e9e6e1;
    --paper: #ffffff;
    --ink-black: #0b0b0c;
    --ink-rule: #1a1a1b;
    --navy: #27306e;
    --royal: #3b4ea6;
    --text-light: #ffffff;
    --brand-blue: #1f3a7a;
  }
  * { margin: 0; padding: 0; box-sizing: border-box; }
  html, body {
    width: 1200px; height: 1200px; overflow: hidden;
    background: var(--page);
    font-family: "Sorts Mill Goudy", Georgia, serif;
  }
  .card {
    position: absolute; left: 126px;
    width: 948px; height: 554px;
    background: var(--paper);
    overflow: hidden;
    box-shadow: 0 6px 18px rgba(0,0,0,.25);
  }
  .card--front { top: 24px; }
  .card--back { top: 614px; }
  .card__art { position: absolute; inset: 0; width: 100%; height: 100%; }

  .brand-mark {
    position: absolute; left: 86px; top: 100px;
    display: flex; align-items: center; gap: 14px;
    color: var(--brand-blue); font-size: 40px; letter-spacing: 2px;
  }
  .brand-mark__dot {
    width: 46px; height: 46px; border-radius: 50%; background: var(--brand-blue);
  }

  .holder { position: absolute; left: 504px; top: 46px; color: var(--text-light); }
  .holder__name { font-size: 38px; letter-spacing: .5px; line-height: 1.1; }
  .holder__title { font-size: 25px; margin-top: 4px; }

  .contact-list { position: absolute; left: 43px; top: 333px; list-style: none; }
  .contact-list li {
    display: flex; align-items: center; gap: 16px;
    height: 40px; color: var(--text-light); font-size: 23px;
  }
  .contact-list svg { width: 21px; height: 21px; flex: none; }

  .back-brand__dot {
    position: absolute; left: 414px; top: 150px;
    width: 120px; height: 120px; border-radius: 50%; background: var(--brand-blue);
  }
  .back-brand__name {
    position: absolute; left: 0; right: 0; top: 322px;
    text-align: center; color: var(--brand-blue);
    font-size: 46px; font-variant: small-caps; letter-spacing: 1px; line-height: 1;
  }
  .back-tagline {
    position: absolute; left: 133px; right: 133px; top: 380px;
    display: flex; align-items: center; justify-content: space-between;
    color: var(--ink-black); font-size: 21px; letter-spacing: 4px;
  }
  .back-tagline__rule { width: 134px; height: 2px; background: var(--ink-rule); }
  .back-url {
    position: absolute; left: 0; right: 0; top: 434px;
    text-align: center; color: var(--brand-blue); font-size: 24px;
  }
</style>
</head>
<body>

<section class="card card--front">
  <svg class="card__art" viewBox="0 0 948 554">
    <defs>
      <linearGradient id="ridgeFill" x1="0" y1="0" x2="0" y2="1">
        <stop offset="0" stop-color="#4656a8"/>
        <stop offset="1" stop-color="#27306e"/>
      </linearGradient>
      <radialGradient id="blackSheen" cx="0.3" cy="0.6" r="0.6">
        <stop offset="0" stop-color="#4a4a4d"/>
        <stop offset="0.45" stop-color="#141415"/>
        <stop offset="1" stop-color="#050505"/>
      </radialGradient>
      <linearGradient id="cornerBlue" x1="0" y1="1" x2="1" y2="0">
        <stop offset="0" stop-color="#27306e"/>
        <stop offset="1" stop-color="#3d58b0"/>
      </linearGradient>
    </defs>
    <path role="img" aria-label="Mountain ridge illustration area" d="M0 236 L 490 236 C 520 320 540 420 612 554 L 0 554 Z" fill="url(#ridgeFill)"/>
    <path d="M444 0 C 430 150 640 230 620 360 C 604 450 612 520 642 554 L 948 554 L 948 0 Z" fill="url(#blackSheen)"/>
    <path d="M636 554 C 790 500 900 420 948 322 L 948 554 Z" fill="url(#cornerBlue)"/>
  </svg>

  <div class="brand-mark"><span class="brand-mark__dot"></span>RLTA</div>

  <div class="holder">
    <div class="holder__name">Dana Whitlow</div>
    <div class="holder__title">Founder and Managing Partner</div>
  </div>

  <ul class="contact-list">
    <li>
      <svg viewBox="0 0 20 20"><rect x="1" y="4" width="18" height="12" fill="none" stroke="#fff" stroke-width="2"/><path d="M1 4 L10 11 L19 4" fill="none" stroke="#fff" stroke-width="2"/></svg>
      dmw@ridgelinetalentco.org
    </li>
    <li>
      <svg viewBox="0 0 20 20"><rect x="1" y="1" width="18" height="18" fill="none" stroke="#fff" stroke-width="1.6"/><path d="M5 8 Q10 4 15 8 L13 10 L11 9 L9 9 L7 10 Z M6 12 H14 V15 H6 Z" fill="#fff"/></svg>
      888.507.3942
    </li>
    <li>
      <svg viewBox="0 0 20 20"><rect x="1" y="1" width="18" height="18" fill="none" stroke="#fff" stroke-width="1.6"/><rect x="6" y="3" width="8" height="14" rx="1" fill="#fff"/><rect x="7.5" y="5" width="5" height="5" fill="#27306e"/></svg>
      5730915.0600
    </li>
    <li>
      <svg viewBox="0 0 20 20"><rect x="1" y="1" width="18" height="18" fill="none" stroke="#fff" stroke-width="1.6"/><rect x="4" y="8" width="12" height="7" fill="#fff"/><rect x="6" y="4" width="8" height="4" fill="#fff"/></svg>
      573.642.1907
    </li>
    <li>
      <svg viewBox="0 0 20 20"><circle cx="10" cy="10" r="8.5" fill="none" stroke="#fff" stroke-width="1.6"/><ellipse cx="10" cy="10" rx="3.5" ry="8.5" fill="none" stroke="#fff" stroke-width="1.3"/><path d="M2 10 H18 M3.5 6 H16.5 M3.5 14 H16.5" stroke="#fff" stroke-width="1.2"/></svg>
      www.ridgelinetalentco.org
    </li>
  </ul>
</section>

<section class="card card--back">
  <svg class="card__art" viewBox="0 0 948 554" aria-hidden="true">
    <defs>
      <linearGradient id="greySweep" x1="0" y1="0" x2="1" y2="0">
        <stop offset="0" stop-color="#1a1a1b"/>
        <stop offset="1" stop-color="#8a8a8d"/>
      </linearGradient>
      <linearGradient id="blueBand" x1="0" y1="0" x2="1" y2="0">
        <stop offset="0" stop-color="#27306e"/>
        <stop offset="0.6" stop-color="#2e3f8f"/>
        <stop offset="1" stop-color="#27306e"/>
      </linearGradient>
      <linearGradient id="blueEdge" x1="0" y1="0" x2="1" y2="0">
        <stop offset="0" stop-color="#2e3f8f"/>
        <stop offset="1" stop-color="#6fb3e0"/>
      </linearGradient>
    </defs>
    <rect x="0" y="0" width="948" height="140" fill="var(--ink-black)"/>
    <path d="M0 116 Q 474 30 948 100 L 948 140 L 0 140 Z" fill="url(#greySweep)"/>
    <path d="M0 128 Q 474 48 948 110 L 948 554 L 0 554 Z" fill="var(--paper)"/>
    <path d="M0 448 Q 474 530 948 430 L 948 554 L 0 554 Z" fill="url(#blueEdge)"/>
    <path d="M0 464 Q 474 534 948 450 L 948 554 L 0 554 Z" fill="url(#blueBand)"/>
  </svg>

  <span class="back-brand__dot"></span>
  <div class="back-brand__name">Ridgeline Talent Associates</div>
  <div class="back-tagline">
    <span class="back-tagline__rule"></span>
    <span>ENERGY RECRUITERS</span>
    <span class="back-tagline__rule"></span>
  </div>
  <div class="back-url">www.ridgelinetalentco.org</div>
</section>

</body>
</html>
```